Barrister in Western Australia needs a fully custom logo, stationery and fonts

Barrister based in Western Australia seeking a fully custom logo, electronic and hardcopy stationery set (including email signature, document headers and footers for use with retainer agreement, invoices, letters of advice etc), custom fonts and business card design. Certain non-optional wording regarding liability limitation has to appear on documents (wording will be supplied but is on the uploaded examples). Have used this platform previously and have outgrown the previous design - samples of which are attached. I live very close to, and spend a significant amount time when not working in or around, the ocean. Use of colours or designs representative of that would be appreciated. The final design should try and communicate strength (of representation), the ability to be flexible (for example, settlements) and the fact I make myself accessible to clients - all factors shown in water/ocean.

Target Market(s)

Legal services providers, solicitors

Industry/Entity Type

Legal

Font styles to use
Serif
Decorative

Requirements
Must have
• Certain insurance wording regarding limitation of liability. Progressive feel to the set including a custom font for use in Office 365. Logo or design that is progressive - can relate to the ocean, water or waves (representing an ability to be fluid, dynamic but inheerent strength)
Nice to have
• Colour
Should not have
• Traditional calligraphy or legal fonts or feel - should not contain any traditional legal industry designs such as pens, scales of justice etc.

```html
<!DOCTYPE html>
<html lang="en">
<head>
<meta charset="utf-8">
<title>Harriet L Monroe – Barrister Stationery</title>
<link rel="stylesheet" href="https://fonts.googleapis.com/css2?family=Cinzel:wght@600&family=Raleway:wght@400&family=Source+Sans+3:ital,wght@0,400;0,700;1,400;1,700&display=swap">
<style>
  :root {
    --stage: #414141;
    --paper: #ffffff;
    --ocean: #2a7fc4;
    --sky: #2a9be0;
    --mark: #2c86c9;
    --mist: #e2eef6;
    --sand: #c9a57a;
    --ink: #2b2b2b;
    --muted: #555555;
  }
  * { margin: 0; padding: 0; box-sizing: border-box; }
  html, body { width: 1200px; height: 720px; overflow: hidden; background: var(--stage); }
  .canvas { position: relative; width: 1200px; height: 720px; }
  .sheet { position: absolute; background: var(--paper); }

  .name {
    font-family: "Cinzel", Georgia, serif;
    font-weight: 600;
    color: var(--ocean);
    white-space: nowrap;
    line-height: 1;
  }
  .role {
    font-family: "Raleway", Arial, sans-serif;
    font-weight: 400;
    color: var(--sky);
    white-space: nowrap;
    line-height: 1;
  }
  .badge { position: absolute; border-radius: 50%; background: var(--mark); }

  /* Letterhead */
  .letterhead { left: 119px; top: 44px; width: 438px; height: 619px; }
  .letterhead .brand { position: absolute; left: 38px; top: 40px; width: 124px; text-align: center; }
  .letterhead .badge { left: 42px; top: 0; width: 40px; height: 40px; }
  .letterhead .name { position: absolute; left: 0; top: 40px; font-size: 13.5px; }
  .letterhead .role { position: absolute; left: 27px; top: 58px; font-size: 7px; letter-spacing: 4.2px; }
  .letterhead .rule { position: absolute; left: 27px; top: 67px; width: 61px; height: 1px; background: var(--ocean); }
  .watermark { position: absolute; left: 83px; top: 182px; width: 272px; height: 272px; border-radius: 50%; background: var(--mist); }
  .sand-rule { position: absolute; left: 38px; top: 511px; width: 73px; height: 1px; background: var(--sand); }
  .contact { position: absolute; left: 38px; top: 518px; font-family: "Source Sans 3", Arial, sans-serif; font-size: 6px; line-height: 8px; color: var(--ink); }
  .contact b { display: inline-block; width: 9px; }
  .disclaimer { position: absolute; left: 38px; top: 554px; width: 240px; font-family: "Source Sans 3", Arial, sans-serif; font-style: italic; font-size: 5px; line-height: 7.2px; color: var(--ink); }

  /* Cards */
  .card-front { left: 652px; top: 64px; width: 475px; height: 296px; }
  .card-front .badge { left: 191px; top: 43px; width: 110px; height: 110px; }
  .card-front .name { position: absolute; left: 0; right: 0; top: 163px; text-align: center; font-size: 42px; }
  .card-front .role { position: absolute; left: 0; right: 0; top: 218px; text-align: center; font-size: 21px; letter-spacing: 19px; text-indent: 19px; }

  .card-back { left: 681px; top: 420px; width: 434px; height: 248px; }
  .card-back .badge { left: 171px; top: 39px; width: 86px; height: 86px; }
  .card-back .name { position: absolute; left: 0; right: 0; top: 124px; text-align: center; font-size: 31px; }
  .card-back .role { position: absolute; left: 0; right: 0; top: 158px; text-align: center; font-size: 14px; letter-spacing: 12px; text-indent: 12px; }
  .card-back .liability { position: absolute; left: 0; right: 0; top: 211px; text-align: center; font-family: "Source Sans 3", Arial, sans-serif; font-style: italic; font-size: 8.5px; color: var(--muted); }
</style>
</head>
<body>
<main class="canvas">
  <section class="sheet letterhead" aria-label="Letterhead">
    <div class="brand">
      <span class="badge"></span>
      <p class="name">Harriet L Monroe</p>
      <p class="role">BARRISTER</p>
      <span class="rule"></span>
    </div>
    <div class="watermark" role="img" aria-label="Faint background mark"></div>
    <span class="sand-rule"></span>
    <div class="contact">
      <p><b>m.</b>+61 (0) 412 555 018</p>
      <p><b>t.</b>+61 8 5550 0142</p>
      <p><b>a.</b>Level 8, 40 Harbour Street, Perth, WA, 6000</p>
    </div>
    <p class="disclaimer"><b>Disclaimer:</b> Liability limited by a scheme approved under Professional Standards Legislation. This email (including any attachments) is confidential and may be privileged. It may be read, copied and used only by the intended recipient. If you have received it in error, please contact the sender immediately by return email. Please then delete both emails and do not disclose their contents to any person.</p>
  </section>

  <section class="sheet card-front" aria-label="Business card front">
    <span class="badge"></span>
    <p class="name">Harriet L Monroe</p>
    <p class="role">BARRISTER</p>
  </section>

  <section class="sheet card-back" aria-label="Business card back">
    <span class="badge"></span>
    <p class="name">Harriet L Monroe</p>
    <p class="role">BARRISTER</p>
    <p class="liability">Liability limited by a scheme approved under Professional Standards Legislation.</p>
  </section>
</main>
</body>
</html>
```